Square Business Cards for Our Restaurant / Event Venue

We need square business cards designed for the management team of our event venue and restaurant. On one side of the card should be the the Harbor Lantern 7 logo and URL www.harborlantern7.example. On the other side should be the Ember Logo and URL www.emberhall7.example. All employee details should be on the side with Ember logo. There will be a total of 5 cards to be created with the design.

Clara Bennquist
clara@harborlantern7.example

main 555.418.3072
direct 555.730.2946

4831 West Orchard Lane SE
Washington, DC 90417

Industry/Entity Type

Business

```html
<!DOCTYPE html>
<html lang="en">
<head>
<meta charset="utf-8">
<title>Harbor Lantern 7 – Square Business Cards</title>
<link rel="stylesheet" href="https://fonts.googleapis.com/css2?family=Arimo&family=Roboto+Condensed:wght@400;700&family=Source+Sans+3:wght@400&display=swap">
<style>
  :root {
    --stage-grey: #e6e7e8;
    --brand-red: #b51e24;
    --paper-white: #ffffff;
    --ink-dark: #231f20;
    --label-grey: #9a9b9d;
    --card-shadow: 0 22px 34px rgba(0, 0, 0, 0.22);
  }
  html, body {
    margin: 0;
    padding: 0;
    overflow: hidden;
  }
  .presentation {
    position: relative;
    width: 1200px;
    height: 825px;
    background: var(--stage-grey);
    overflow: hidden;
  }
  .card {
    position: absolute;
    top: 102px;
    width: 480px;
    height: 480px;
    box-shadow: var(--card-shadow);
  }
  .card--front {
    left: 98px;
    background: var(--paper-white);
  }
  .card--back {
    left: 638px;
    background: var(--brand-red);
    color: var(--paper-white);
    font-family: "Roboto Condensed", "Arial Narrow", sans-serif;
  }
  .venue-mark {
    position: absolute;
    left: 106px;
    top: 89px;
    width: 268px;
    height: 268px;
    border-radius: 50%;
    background: var(--brand-red);
    display: flex;
    align-items: center;
    justify-content: center;
    text-align: center;
  }
  .venue-mark__name {
    font-family: "Source Sans 3", "Myriad Pro", sans-serif;
    font-weight: 400;
    font-size: 34px;
    line-height: 1.15;
    color: var(--paper-white);
  }
  .front-url {
    position: absolute;
    left: 0;
    right: 0;
    top: 406px;
    text-align: center;
    font-family: "Source Sans 3", "Myriad Pro", sans-serif;
    font-size: 21px;
    line-height: 1;
    color: var(--ink-dark);
  }
  .back-line {
    position: absolute;
    left: 95px;
    margin: 0;
    line-height: 1;
    white-space: nowrap;
  }
  .brand-name {
    left: 92px;
    top: 62px;
    font-weight: 700;
    font-size: 72px;
    color: var(--ink-dark);
  }
  .brand-url { left: 92px; top: 178px; font-size: 19px; }
  .person-name { top: 233px; font-size: 22px; font-weight: 700; }
  .person-email { top: 268px; font-size: 20px; }
  .person-phones { top: 302px; font-size: 20px; }
  .phone-divider {
    display: inline-block;
    width: 1px;
    height: 21px;
    background: var(--paper-white);
    margin: 0 14px 0 15px;
    vertical-align: -4px;
  }
  .address-street { top: 370px; font-size: 20px; }
  .address-city { top: 403px; font-size: 20px; }
  .side-label {
    position: absolute;
    top: 704px;
    width: 480px;
    text-align: center;
    font-family: "Arimo", Arial, sans-serif;
    font-size: 30px;
    line-height: 1;
    color: var(--label-grey);
  }
  .side-label--front { left: 98px; }
  .side-label--back { left: 638px; }
</style>
</head>
<body>
<main class="presentation">
  <section class="card card--front" aria-label="Card front">
    <div class="venue-mark">
      <span class="venue-mark__name">Harbor Lantern 7</span>
    </div>
    <p class="front-url" style="margin:0">www.harborlantern7.example</p>
  </section>

  <section class="card card--back" aria-label="Card back">
    <p class="back-line brand-name">Ember</p>
    <p class="back-line brand-url">www.emberhall7.example</p>
    <p class="back-line person-name">Clara Bennquist</p>
    <p class="back-line person-email">clara@harborlantern7.example</p>
    <p class="back-line person-phones">main 555.418.3072<span class="phone-divider"></span>direct 555.730.2946</p>
    <p class="back-line address-street">4831 West Orchard Lane SE</p>
    <p class="back-line address-city">Washington, DC 90417</p>
  </section>

  <p class="side-label side-label--front" style="margin:0">Front Side</p>
  <p class="side-label side-label--back" style="margin:0">Back Side</p>
</main>
</body>
</html>
```